Innovative Consulting Firm Needs New Business Cards and Stationary

Our Innovative Consulting Firm, Larkfield Consulting, is in need of new business cards and stationary designs. We want two-sided cards that incorporate our logo, which is attached. We are looking for something not too formal, but is professional and slick.

Card should have the following information:
Name (ex. Tom Bradley)
Title (ex. Manager)
Address (ex. 24680 Cedar Lane)
Address 2 (ex. Suite 100)
City
State
Zip Code
Mobile
Email

The card should also have our website: www.larkfieldconsulting.example

Industry/Entity Type

Management Consulting

Contact Information for Business Card

Name (ex. Tom Bradley)
Title (ex. Manager)
Address 2 (ex. Suite 100)
City
State
Zip Code
Mobile
Email

Font styles to use
Sans Serif

Requirements
Must have
• The colors on the card must match the colors in the logo. The exact color codes are attached in a pdf.
Nice to have
• The Company's Tagline is "Focused on your Future". This might be nice to incorporate, but not necessary.

```html
<!DOCTYPE html>
<html lang="en">
<head>
<meta charset="utf-8">
<title>Larkfield Consulting – Business Cards</title>
<link href="https://fonts.googleapis.com/css2?family=Lato:wght@400;700&display=swap" rel="stylesheet">
<style>
  :root{
    --backdrop:#d9d9d9;
    --card:#ffffff;
    --navy:#1f4e86;
    --gold:#f2ae1c;
    --shadow:rgba(0,0,0,.18);
  }
  *{margin:0;padding:0;box-sizing:border-box}
  html,body{width:1200px;height:900px;overflow:hidden}
  body{
    background:var(--backdrop);
    font-family:"Lato",Arial,sans-serif;
    display:flex;align-items:center;justify-content:center;gap:40px;
  }
  .card{
    position:relative;width:540px;height:310px;background:var(--card);
    box-shadow:0 6px 18px var(--shadow);overflow:hidden;
  }
  .swoosh{position:absolute;inset:0;width:100%;height:100%}
  .holder{position:absolute;left:34px;top:28px}
  .holder-name{color:var(--navy);font-weight:700;font-size:15px;letter-spacing:.3px}
  .holder-title{color:var(--gold);font-size:10px;letter-spacing:.6px;margin-top:2px}
  .contact{position:absolute;left:34px;top:146px;list-style:none}
  .contact li{display:flex;align-items:center;gap:8px;color:var(--navy);font-size:11px;line-height:18px;white-space:nowrap}
  .contact svg{width:10px;height:10px;flex:none}
  .wordmark{position:absolute;color:var(--navy);font-weight:700;text-align:right}
  .wordmark-name{display:block;font-size:40px;line-height:1;letter-spacing:-.5px}
  .wordmark-sub{display:block;font-size:10px;letter-spacing:4px;margin-top:3px}
  .card-front .wordmark{right:34px;top:120px}
  .card-back .wordmark{right:40px;top:190px}
</style>
</head>
<body>

<section class="card card-front">
  <svg class="swoosh" viewBox="0 0 540 310" aria-hidden="true">
    <path d="M50 60 Q380 120 410 310 L384 310 Q350 140 50 60 Z" fill="var(--gold)"/>
  </svg>

  <div class="holder">
    <p class="holder-name">TOM BRADLEY</p>
    <p class="holder-title">MANAGER</p>
  </div>

  <ul class="contact">
    <li><svg viewBox="0 0 12 12"><path d="M2.5 1h2l1 3-1.3 1a6 6 0 0 0 2.8 2.8l1-1.3 3 1v2a1 1 0 0 1-1 1A9 9 0 0 1 1.5 2a1 1 0 0 1 1-1z" fill="var(--gold)"/></svg>0770-5550-1842</li>
    <li><svg viewBox="0 0 12 12"><rect x="1" y="2.5" width="10" height="7" fill="none" stroke="var(--gold)" stroke-width="1.3"/><path d="M1 2.5l5 4 5-4" fill="none" stroke="var(--gold)" stroke-width="1.3"/></svg>tbradley@larkfield.example</li>
    <li><svg viewBox="0 0 12 12"><rect x="1.5" y="1.5" width="9" height="9" fill="none" stroke="var(--gold)" stroke-width="1.3"/></svg>www.larkfieldconsulting.example</li>
    <li><svg viewBox="0 0 12 12"><path d="M6 11.5S2 7 2 4.5a4 4 0 0 1 8 0C10 7 6 11.5 6 11.5z" fill="var(--gold)"/><circle cx="6" cy="4.5" r="1.4" fill="#fff"/></svg>24680 Cedar Lane, Suite 100, City, State, Zip Code</li>
  </ul>

  <div class="wordmark">
    <span class="wordmark-name">Larkfield</span>
    <span class="wordmark-sub">CONSULTING</span>
  </div>
</section>

<section class="card card-back">
  <div class="wordmark">
    <span class="wordmark-name">Larkfield</span>
    <span class="wordmark-sub">CONSULTING</span>
  </div>
</section>

</body>
</html>
```